Spiral Bound Classy Marketing Planner Cover Design

A5 marketing planner book cover requiredClassy, minimalist design for female entrepreneurs. The inside is all in grey and is a minimalist uncluttered design. Name of the planner is It's Time Marketing Recipe PlannerHeader font inside the planner is Shelby and other font is Lato Brand colours are teal and grey.The printing format has changed and as such I am looking for a new cover design to make this marketing planner look classy and engaging. Would prefer my logo to be on the back. We have the option for a 10cm x 10cm foil detail to be added on the front cover, feel free to add this to your design.This is for a spiral bound book - A5 front cover and A5 back cover - no spine required.

Target Market(s)

Female entrepreneurs

Industry/Entity Type

Marketing

Colors
33b8a4
ffffff

Requirements
Must have
• Front and back designs
• A5
Should not have
• Large illustrations
• People in the design
• Spine design

```html
<!DOCTYPE html>
<html lang="en">
<head>
<meta charset="utf-8">
<title>Bright Path Promotion Blueprint Planner – Covers</title>
<link rel="stylesheet" href="https://fonts.googleapis.com/css2?family=Jost:wght@500;700&family=Lato:wght@700&display=swap">
<style>
  :root {
    --backdrop: #6e6e6e;
    --cover-pink: #ecd5d4;
    --panel-white: #ececec;
    --brand-teal: #33b8a4;
    --brand-grey: #444444;
    --tag-grey: #8d8d8d;
  }
  * { margin: 0; padding: 0; box-sizing: border-box; }
  html, body {
    width: 1200px;
    height: 742px;
    overflow: hidden;
    background: var(--backdrop);
  }
  .spread {
    position: relative;
    width: 1200px;
    height: 742px;
  }
  .cover {
    position: absolute;
    top: 101px;
    width: 380px;
    height: 540px;
    background: var(--cover-pink);
  }
  .cover--back { left: 150px; }
  .cover--front { left: 670px; }

  /* Back cover brand block */
  .brand {
    position: absolute;
    left: 0;
    right: 0;
    top: 200px;
    text-align: center;
    font-family: 'Lato', sans-serif;
  }
  .brand__name {
    font-family: 'Jost', sans-serif;
    font-weight: 700;
    color: var(--brand-teal);
    font-size: 30px;
    line-height: 1.1;
  }
  .brand__tagline {
    margin-top: 18px;
    color: var(--tag-grey);
    font-size: 7px;
    letter-spacing: 1.6px;
    line-height: 1.4;
    text-transform: uppercase;
  }

  /* Front cover title panel */
  .title-panel {
    position: absolute;
    left: 86px;
    top: 138px;
    width: 253px;
    height: 244px;
    background: var(--panel-white);
    display: flex;
    flex-direction: column;
    justify-content: center;
    align-items: center;
    font-family: 'Jost', sans-serif;
    text-transform: uppercase;
    white-space: nowrap;
  }
  .title-panel__lead {
    color: var(--brand-teal);
    font-weight: 700;
    font-size: 33px;
    line-height: 1;
    letter-spacing: -0.3px;
  }
  .title-panel__sub {
    color: var(--brand-grey);
    font-weight: 500;
    font-size: 18px;
    line-height: 1.1;
    margin-top: 5px;
  }
  .title-panel__main {
    color: var(--brand-grey);
    font-weight: 700;
    font-size: 46px;
    line-height: 1;
    letter-spacing: -0.5px;
  }
</style>
</head>
<body>
  <main class="spread">
    <section class="cover cover--back" aria-label="Back cover">
      <div class="brand">
        <p class="brand__name">The Promo<br>Pantry</p>
        <p class="brand__tagline">Promotion with clear steps<br>toward steady growth</p>
      </div>
    </section>

    <section class="cover cover--front" aria-label="Front cover">
      <div class="title-panel">
        <h1 class="title-panel__lead">Bright Path</h1>
        <p class="title-panel__sub">Promotion Blueprint</p>
        <p class="title-panel__main">Planner</p>
      </div>
    </section>
  </main>
</body>
</html>
```